Simple graphic for a book or slide presentation

We are looking for a style that suits the style of our book. It's title is Venture. Thriving boldly on uncertain ground. There will be more line drawing/graphics in the book but how you design this image will create the style for all the other simple graphics in the book (once we decide what they are). So this one design will lead to a few more to match the style of this one. We'd like the shape of the overall graphic (i.e the arrows and words/bubbles) to be circular (not a rounded square as appears in the sample attached). Perhaps the words don't need to be in ovals or bound by anything at all; perhaps they do - let's see what you see. We'd like you to choose a font or offer many different fonts you think will capture the practical yet unconventional tone of the book. The book is teaching that managing risks in life is a life-skill that can be learned. The section of the book where this graphic will be placed is called "the power of language" - basically we are saying that thoughts, words and actions create our culture and our destiny. This insight comes from Pranav Kelkari's famous quote:
Carefully watch your thoughts, for they become your words.
Manage and watch your words, for they will become your actions.
Consider and judge your actions, for they have become your habits.
Acknowledge and watch your habits, for they shall become your values.
Understand and embrace your values, for they become your destiny.

Please change the text in the middle of the graphic to say: The Human Culture Cycle

```html
<!DOCTYPE html>
<html lang="en">
<head>
<meta charset="utf-8">
<title>The Human Culture Cycle</title>
<link rel="stylesheet" href="https://fonts.googleapis.com/css2?family=Open+Sans:wght@700;800&display=swap">
<style>
  :root {
    --paper: #ffffff;
    --ink: #111111;
    --ring: #666666;
    --arrow: #595959;
  }
  * { margin: 0; padding: 0; box-sizing: border-box; }
  html, body {
    width: 1200px;
    height: 1000px;
    overflow: hidden;
    background: var(--paper);
  }
  .cycle-graphic {
    position: relative;
    width: 1200px;
    height: 1000px;
    font-family: "Open Sans", Arial, sans-serif;
    color: var(--ink);
  }
  .cycle-lines {
    position: absolute;
    inset: 0;
  }
  .stage-ring {
    fill: var(--paper);
    stroke: var(--ring);
    stroke-width: 3;
  }
  .flow-arrow {
    fill: none;
    stroke: var(--arrow);
    stroke-width: 14;
  }
  .arrow-head { fill: var(--arrow); }
  .stage-label {
    position: absolute;
    width: 160px;
    margin-left: -80px;
    margin-top: -18px;
    text-align: center;
    font-weight: 700;
    font-size: 25px;
    line-height: 36px;
  }
  .cycle-title {
    position: absolute;
    left: 0;
    top: 381px;
    width: 1200px;
    text-align: center;
    font-weight: 700;
    font-size: 38px;
    line-height: 64px;
    letter-spacing: 0.62em;
    text-indent: 0.62em;
  }
</style>
</head>
<body>
<main class="cycle-graphic">
  <svg class="cycle-lines" width="1200" height="1000" viewBox="0 0 1200 1000" aria-hidden="true">
    <defs>
      <marker id="arrow-tip" markerUnits="userSpaceOnUse" markerWidth="40" markerHeight="36"
              refX="4" refY="17" orient="auto">
        <path class="arrow-head" d="M0,0 L36,17 L0,34 Z"/>
      </marker>
    </defs>

    <path class="flow-arrow" marker-end="url(#arrow-tip)" d="M688.7,194.5 A322,322 0 0 1 798,250"/>
    <path class="flow-arrow" marker-end="url(#arrow-tip)" d="M906.2,404.5 A322,322 0 0 1 913,570"/>
    <path class="flow-arrow" marker-end="url(#arrow-tip)" d="M819.6,739.5 A322,322 0 0 1 715,803"/>
    <path class="flow-arrow" marker-end="url(#arrow-tip)" d="M511.3,813.5 A322,322 0 0 1 402,755"/>
    <path class="flow-arrow" marker-end="url(#arrow-tip)" d="M289,587.3 A322,322 0 0 1 286,438"/>
    <path class="flow-arrow" marker-end="url(#arrow-tip)" d="M393,257.3 A322,322 0 0 1 485,205"/>

    <circle class="stage-ring" cx="598" cy="182" r="80"/>
    <circle class="stage-ring" cx="860" cy="326" r="80"/>
    <circle class="stage-ring" cx="860" cy="692" r="80"/>
    <circle class="stage-ring" cx="598" cy="818" r="80"/>
    <circle class="stage-ring" cx="340" cy="692" r="80"/>
    <circle class="stage-ring" cx="340" cy="326" r="80"/>
  </svg>

  <div class="stage-label" style="left:598px; top:177px;">Thoughts</div>
  <div class="stage-label" style="left:860px; top:327px;">Words</div>
  <div class="stage-label" style="left:860px; top:695px;">Actions</div>
  <div class="stage-label" style="left:598px; top:823px;">Habits</div>
  <div class="stage-label" style="left:340px; top:695px;">Values</div>
  <div class="stage-label" style="left:340px; top:327px;">Culture</div>

  <h1 class="cycle-title">THE<br>HUMAN<br>CULTURE<br>CYCLE</h1>
</main>
</body>
</html>
```